Meadowlark Learning Growth Partners (MLGP)

This is a professional business card. Logo and picture are a must on the front of the card. I am an educational consultant. I have been consulting for the past three years for a company. I am now opening my own company. My goal for my consulting company is to eventually consult all over America.

Target Market(s)

Educators, schools, professionals

Industry/Entity Type

Consulting

Contact Information for Business Card

Picture/logo on front, simple modern design

Font styles to use
Serif

Colors
85abd2
0355a3
3176b5
cedeed

Requirements
Must have
• picture, logo,
• Odessa Pruitt, Ed.S
• address 5073 Cormorant ridge Dr. Nashville, TN 37940
• Cell:616-555-0148
• Office: 629-555-0172
• www.Mlgpedu.example
• pruittodessa@mailbox.example

```html
<!DOCTYPE html>
<html lang="en">
<head>
<meta charset="utf-8">
<title>MLGP Business Card</title>
<link href="https://fonts.googleapis.com/css2?family=Tinos:wght@400;700&family=Montserrat:wght@700;800&display=swap" rel="stylesheet">
<style>
  :root {
    --navy: #1d3a6e;
    --ink: #1f3566;
    --paper: #ffffff;
    --stage: #e9edf2;
    --photo-light: #d9dde3;
    --photo-dark: #2a2f3a;
  }
  * { box-sizing: border-box; margin: 0; padding: 0; }
  html, body { width: 1200px; height: 780px; overflow: hidden; }
  body {
    background: var(--stage);
    position: relative;
    font-family: "Tinos", "Times New Roman", serif;
  }
  .card {
    position: absolute;
    top: 238px;
    width: 530px;
    height: 303px;
    overflow: hidden;
    box-shadow: 0 6px 18px rgba(0,0,0,0.18);
  }
  /* Back of card */
  .card-back {
    left: 45px;
    background: var(--navy);
    color: var(--paper);
  }
  .back-mark {
    position: absolute;
    left: 0; right: 0; top: 108px;
    display: flex; align-items: center; justify-content: center; gap: 12px;
  }
  .back-mark .dot {
    width: 14px; height: 14px; border-radius: 50%; background: var(--paper);
  }
  .back-mark .wordmark {
    font-family: "Montserrat", Arial, sans-serif;
    font-weight: 800;
    font-size: 54px;
    letter-spacing: 3px;
  }
  .back-url {
    position: absolute;
    left: 0; right: 0; top: 196px;
    text-align: center;
    font-size: 13px;
    letter-spacing: 3px;
  }
  /* Front of card */
  .card-front {
    left: 625px;
    background: var(--paper);
    color: var(--ink);
  }
  .brand {
    position: absolute;
    left: 30px; top: 30px;
    display: flex; align-items: center;
  }
  .brand .dot {
    width: 12px; height: 12px; border-radius: 50%; background: var(--ink); margin-right: 10px;
  }
  .brand .wordmark {
    font-family: "Montserrat", Arial, sans-serif;
    font-weight: 800;
    font-size: 28px;
    letter-spacing: 2px;
  }
  .brand .divider {
    width: 1px; height: 56px; background: var(--ink); margin: 0 12px;
  }
  .brand .company {
    font-family: "Montserrat", Arial, sans-serif;
    font-weight: 700;
    font-size: 13px;
    line-height: 1.12;
  }
  .person {
    position: absolute;
    left: 30px; top: 122px;
    width: 248px;
  }
  .person-name {
    font-size: 16px;
    letter-spacing: 0.5px;
    padding-bottom: 6px;
    border-bottom: 1px solid var(--ink);
  }
  .contacts {
    list-style: none;
    margin-top: 8px;
    font-size: 12.5px;
    line-height: 1.35;
  }
  .contacts li { display: flex; align-items: center; gap: 7px; white-space: nowrap; }
  .contacts svg { width: 10px; height: 10px; flex: none; }
  .base-band {
    position: absolute;
    left: 0; bottom: 0;
    width: 330px; height: 18px;
    background: var(--navy);
  }
  .portrait {
    position: absolute;
    right: 0; bottom: 0;
    width: 210px; height: 195px;
    background: linear-gradient(180deg, var(--photo-light) 0%, #c9b796 35%, var(--photo-dark) 100%);
  }
</style>
</head>
<body>
  <section class="card card-back" aria-label="Back of business card">
    <div class="back-mark">
      <span class="dot"></span>
      <span class="wordmark">MLGP</span>
    </div>
    <p class="back-url">www.Mlgpedu.example</p>
  </section>

  <section class="card card-front" aria-label="Front of business card">
    <div class="brand">
      <span class="dot"></span>
      <span class="wordmark">MLGP</span>
      <span class="divider"></span>
      <span class="company">Meadowlark<br>Learning<br>Growth<br>Partners</span>
    </div>

    <div class="person">
      <h1 class="person-name">ODESSA PRUITT, ED.S</h1>
      <ul class="contacts">
        <li>
          <svg viewBox="0 0 10 10"><rect x="2" y="0.5" width="6" height="9" rx="1" fill="none" stroke="currentColor" stroke-width="1.2"/></svg>
          616-555-0148
        </li>
        <li>
          <svg viewBox="0 0 10 10"><path d="M1 4 Q5 0 9 4 L8 5 L6 4 L4 4 L2 5 Z M2 6 H8 V9 H2 Z" fill="currentColor"/></svg>
          629-555-0172
        </li>
        <li>
          <svg viewBox="0 0 10 10"><rect x="0.5" y="2" width="9" height="6.5" fill="currentColor"/><path d="M0.5 2 L5 5.5 L9.5 2" fill="none" stroke="#fff" stroke-width="1"/></svg>
          pruittodessa@mailbox.example
        </li>
        <li>
          <svg viewBox="0 0 10 10"><path d="M5 9.5 C2 6 2 4.5 2 3.8 A3 3 0 0 1 8 3.8 C8 4.5 8 6 5 9.5 Z" fill="none" stroke="currentColor" stroke-width="1.1"/><circle cx="5" cy="3.8" r="1" fill="currentColor"/></svg>
          5073 Cormorant ridge Dr. Nashville, TN 37940
        </li>
      </ul>
    </div>

    <div class="base-band"></div>
    <div class="portrait" role="img" aria-label="Professional portrait photo of Odessa Pruitt"></div>
  </section>
</body>
</html>
```